Lone Prairie Canvas & Sound Jubilee

Organization:
Lone Prairie Canvas and Sound Jubilee is a non-profit organization created by a group of anonymous donors to bring more fun, culture, and art to a small Texas town. Our mission is to promote art and music in Washington County.
The multi-day eclectic festival will feature three stages, a film, art vendors, live mural artists, and food trucks set up throughout historic downtown Brenham. The event is FREE to the public.
Goals:
We need an attractive poster to publicize the festival.
Details:
Lone Prairie Canvas and Sound Jubilee
Friday, October 14 – 16
Free admission (VIP tickets available)
Live music- 3 stages/10 bands
Film Screening
Art vendors and art walk
Live art murals
Food trucks
www.loneprairiecanvasandsoundjubilee.example
#loneprairiecanvasandsound
Requirements:
Please incorporate our festival logo attached.
Conclusion:
After selecting a poster design, we hope to continue to work with the artist to design other event materials including website splash page and rack cards using design elements from the poster.

```html
<!DOCTYPE html>
<html lang="en">
<head>
<meta charset="utf-8">
<title>Lone Prairie Canvas &amp; Sound Jubilee — Poster</title>
<link rel="stylesheet" href="https://fonts.googleapis.com/css2?family=Roboto+Condensed:wght@400;700&family=Arimo:wght@400;700&family=Saira+Condensed:wght@400;500&family=Cinzel:wght@700;900&family=Crimson+Text:wght@600&display=swap">
<style>
  :root {
    --page: #e4e6e9;
    --black: #070707;
    --red: #d3151b;
    --red-deep: #8e0c10;
    --white: #ffffff;
    --silver: #d9d9d9;
    --ink: #111111;
  }
  * { box-sizing: border-box; margin: 0; padding: 0; }
  html, body { width: 900px; height: 1200px; overflow: hidden; }
  body { background: var(--page); position: relative; }

  .poster {
    position: absolute; left: 65px; top: 58px;
    width: 772px; height: 1082px;
    background: var(--black); overflow: hidden;
    box-shadow: 0 4px 14px rgba(0,0,0,.35);
  }
  .photo { position: absolute; }
  .photo--stage { left: 0; top: 0; width: 575px; height: 500px;
    background: radial-gradient(ellipse at 55% 45%, #c2231d 0 18%, transparent 40%),
                linear-gradient(135deg, #1d3a6e 0%, #4a78b4 40%, #23324f 75%, #0e1626 100%); }
  .photo--guitarist { left: 575px; top: 0; width: 197px; height: 252px;
    background: linear-gradient(160deg, #1a1a1a, #6e6e6e 55%, #0c0c0c); }
  .photo--singer { left: 575px; top: 252px; width: 197px; height: 248px;
    background: linear-gradient(200deg, #c9cbc8, #6b6f6a 50%, #1d1f1c); }
  .photo--audience { left: 0; top: 327px; width: 235px; height: 180px;
    background: linear-gradient(180deg, #bfc3c4, #5f554c 60%, #2a2420); }
  .photo--crowd { left: 345px; top: 812px; width: 427px; height: 270px;
    background: radial-gradient(ellipse at 60% 100%, #6a6a6a 0%, #2a2a2a 55%, transparent 85%); opacity: .85; }

  .waves { position: absolute; left: 0; top: 0; }

  .banner {
    position: absolute; left: 45px; top: 0; width: 190px; height: 217px;
    background: var(--white);
    clip-path: polygon(0 0, 100% 0, 100% 100%, 50% 88%, 0 100%);
    display: flex; align-items: center; justify-content: center;
    padding: 0 16px 30px;
  }
  .banner__name {
    font-family: "Roboto Condensed", sans-serif; font-weight: 700;
    font-size: 22px; line-height: 1.1; text-align: center; color: var(--ink);
    text-transform: uppercase;
  }

  .rule { position: absolute; width: 2px; background: var(--white); top: 520px; height: 470px; }
  .rule--left { left: 25px; }
  .rule--right { left: 745px; top: 540px; height: 460px; }

  .highlights {
    position: absolute; left: 63px; top: 614px; width: 252px; height: 358px;
    background: linear-gradient(180deg, var(--red) 0%, #c1121a 100%);
    padding: 104px 0 0 12px; list-style: none; overflow: hidden;
  }
  .highlights li {
    display: flex; align-items: flex-start; gap: 9px;
    font-family: "Saira Condensed", sans-serif; font-weight: 500; font-size: 18px;
    line-height: 30px; color: var(--white); text-transform: uppercase;
    white-space: nowrap; margin-bottom: 7px;
  }
  .highlights svg { flex: none; margin-top: 8px; }

  .title { position: absolute; left: 355px; width: 380px; text-align: center; color: var(--white); }
  .title__top { top: 640px; font-family: "Roboto Condensed", sans-serif; font-weight: 700;
    font-size: 42px; line-height: 1; color: var(--silver);
    background: linear-gradient(180deg, #ffffff 0%, #d6d6d6 55%, #9a9a9a 100%);
    -webkit-background-clip: text; background-clip: text; -webkit-text-fill-color: transparent; }
  .title__and { top: 716px; height: 24px; }
  .title__and::before { content: ""; position: absolute; left: 0; right: 0; top: 11px; height: 2px; background: var(--white); }
  .title__and span { position: relative; display: inline-block; background: var(--white);
    color: var(--red); font-family: "Arimo", sans-serif; font-weight: 700; font-size: 18px;
    padding: 1px 26px; border-radius: 50%; line-height: 22px; }
  .title__bottom { top: 752px; font-family: "Arimo", sans-serif; font-size: 33px; letter-spacing: 1px; line-height: 1; color: #e8e8e8; }
  .title__line { top: 800px; height: 3px; background: linear-gradient(90deg, transparent, var(--red) 15%, var(--red) 85%, transparent); }

  .date { position: absolute; left: 380px; width: 320px; text-align: center; line-height: 1; }
  .date__day { top: 832px; font-family: "Cinzel", serif; font-weight: 700; font-size: 32px; color: var(--white); }
  .date__month { top: 870px; font-family: "Cinzel", serif; font-weight: 900; font-size: 44px; color: var(--red);
    -webkit-text-stroke: 1px #ffffff; }
  .date__range { top: 918px; font-family: "Crimson Text", serif; font-weight: 600; font-size: 54px; color: var(--white); }

  .web-bar {
    position: absolute; left: 45px; top: 1002px; width: 680px; height: 28px;
    background: linear-gradient(90deg, transparent 0%, var(--red-deep) 8%, var(--red) 30%, var(--red) 90%, var(--red-deep) 100%);
    display: flex; align-items: center; justify-content: center;
    font-family: "Arimo", sans-serif; font-weight: 700; font-size: 14px; color: var(--white);
  }
</style>
</head>
<body>
<main class="poster">
  <div class="photo photo--stage" role="img" aria-label="Photo of a singer in a red jacket performing on stage with a band"></div>
  <div class="photo photo--guitarist" role="img" aria-label="Black and white photo of a guitarist kneeling on stage"></div>
  <div class="photo photo--singer" role="img" aria-label="Photo of a performer with sunglasses outdoors"></div>
  <div class="photo photo--audience" role="img" aria-label="Photo of a band seated backstage"></div>
  <div class="photo photo--crowd" role="img" aria-label="Faded photo of a concert crowd with raised hands"></div>

  <svg class="waves" width="772" height="1082" viewBox="0 0 772 1082" aria-hidden="true">
    <path d="M0,505 C220,525 470,470 772,440 L772,1082 L0,1082 Z" fill="#070707"/>
    <path d="M0,530 C170,505 320,560 500,528 C620,506 700,482 772,472 L772,500 C650,518 520,560 390,592 C250,628 140,664 40,672 L0,668 Z" fill="#d3151b"/>
    <path d="M0,560 C150,585 260,560 400,590 C250,630 130,662 0,672 Z" fill="#a50e13"/>
    <path d="M0,548 C190,580 430,520 772,466" fill="none" stroke="#ffffff" stroke-width="6"/>
    <path d="M0,520 C200,500 420,535 772,458" fill="none" stroke="#ffffff" stroke-width="2" opacity=".7"/>
  </svg>

  <div class="banner">
    <p class="banner__name">Lone Prairie Canvas &amp; Sound Jubilee</p>
  </div>

  <span class="rule rule--left"></span>
  <span class="rule rule--right"></span>

  <ul class="highlights">
    <li><svg width="14" height="14" viewBox="0 0 14 14"><circle cx="7" cy="7" r="6" fill="none" stroke="#fff" stroke-width="1.4"/><path d="M5.5 4 L8.5 7 L5.5 10" fill="none" stroke="#fff" stroke-width="1.6"/></svg><span>Free admission<br>(VIP tickets available)</span></li>
    <li><svg width="14" height="14" viewBox="0 0 14 14"><circle cx="7" cy="7" r="6" fill="none" stroke="#fff" stroke-width="1.4"/><path d="M5.5 4 L8.5 7 L5.5 10" fill="none" stroke="#fff" stroke-width="1.6"/></svg><span>Live music- 3 stages/10 bands</span></li>
    <li><svg width="14" height="14" viewBox="0 0 14 14"><circle cx="7" cy="7" r="6" fill="none" stroke="#fff" stroke-width="1.4"/><path d="M5.5 4 L8.5 7 L5.5 10" fill="none" stroke="#fff" stroke-width="1.6"/></svg><span>Film screening</span></li>
    <li><svg width="14" height="14" viewBox="0 0 14 14"><circle cx="7" cy="7" r="6" fill="none" stroke="#fff" stroke-width="1.4"/><path d="M5.5 4 L8.5 7 L5.5 10" fill="none" stroke="#fff" stroke-width="1.6"/></svg><span>Art vendors and art walk</span></li>
    <li><svg width="14" height="14" viewBox="0 0 14 14"><circle cx="7" cy="7" r="6" fill="none" stroke="#fff" stroke-width="1.4"/><path d="M5.5 4 L8.5 7 L5.5 10" fill="none" stroke="#fff" stroke-width="1.6"/></svg><span>Live art murals</span></li>
    <li><svg width="14" height="14" viewBox="0 0 14 14"><circle cx="7" cy="7" r="6" fill="none" stroke="#fff" stroke-width="1.4"/><path d="M5.5 4 L8.5 7 L5.5 10" fill="none" stroke="#fff" stroke-width="1.6"/></svg><span>Food trucks</span></li>
  </ul>

  <h1 class="title title__top">Lone Prairie Canvas</h1>
  <div class="title title__and"><span>and</span></div>
  <p class="title title__bottom">SOUND JUBILEE</p>
  <div class="title title__line"></div>

  <p class="date date__day">Friday</p>
  <p class="date date__month">October</p>
  <p class="date date__range">14 to 16</p>

  <p class="web-bar">www.loneprairiecanvasandsoundjubilee.example</p>
</main>
</body>
</html>
```